Quillmarsh Property Solutions need a business card design

Hello guys. We would need a business card design asap please.
We are a start up property investment business based in London UK specialised in buying, selling, managing and letting properties and helping distressed property owners.
The name of our Business is Quillmarsh, the logo symbolises the four fundamental elements of the world (earth, air, fire and water) and so it stands for strength, stability, longevity.
We would like the business card to communicate professionalism and reliability. Many many thanks indeed for your work.

Details:

1.) Rosalind Opaleye
Property Investor
Mobile: +44(0)7700361752
Email: rosalind.quillmarsh@brindlepost.co.uk

2.) Anselm Opaleye
Property Investor
Mobile: +44(0)7700584029
Email: anselm.quillmarsh@brindlepost.co.uk

Investment

```html
<!DOCTYPE html>
<html lang="en">
<head>
<meta charset="utf-8">
<title>Quillmarsh Property Solutions — Business Card</title>
<link rel="stylesheet" href="https://fonts.googleapis.com/css2?family=Lato:wght@300;400;700&display=swap">
<style>
  :root {
    --backdrop: #e9e4dc;
    --card: #ffffff;
    --card-shade: #f1f1f1;
    --ink: #4a4a4a;
    --ink-soft: #6d6d6d;
    --red: #d4283a;
    --blue: #3f7cc4;
    --green: #1f9a4a;
  }
  * { box-sizing: border-box; margin: 0; padding: 0; }
  html, body { width: 704px; height: 1200px; overflow: hidden; }
  body {
    background: var(--backdrop);
    font-family: "Lato", sans-serif;
    color: var(--ink);
    display: flex;
    flex-direction: column;
    align-items: center;
    justify-content: center;
    gap: 120px;
  }
  .card {
    position: relative;
    width: 580px;
    height: 330px;
    border-radius: 18px;
    background: linear-gradient(160deg, var(--card) 55%, var(--card-shade));
    box-shadow: 0 6px 18px rgba(0,0,0,.18);
    overflow: hidden;
  }
  .edge-band {
    position: absolute;
    top: 0; right: 0;
    width: 24px; height: 100%;
    display: flex; flex-direction: column;
  }
  .edge-band span { flex: 1; }
  .red { background: var(--red); }
  .blue { background: var(--blue); }
  .green { background: var(--green); }

  .brand {
    display: flex; align-items: center; gap: 14px;
  }
  .brand-mark { width: 16px; height: 16px; background: var(--ink); flex: none; }
  .brand-name {
    font-weight: 700;
    font-size: 38px;
    letter-spacing: 2px;
    text-transform: uppercase;
    color: var(--ink);
    line-height: 1.05;
  }
  .brand-name small { display: block; font-size: 17px; letter-spacing: 1.5px; }

  .card-front .brand { position: absolute; left: 60px; top: 50%; transform: translateY(-50%); }

  .card-back .contact {
    position: absolute; right: 62px; top: 42px;
    text-align: right;
  }
  .person-name { font-size: 24px; font-weight: 400; color: var(--red); }
  .person-role { font-size: 16px; color: var(--blue); margin-top: 2px; }
  .contact-line {
    display: flex; justify-content: flex-end; align-items: center; gap: 8px;
    font-size: 14px; font-weight: 300; color: var(--ink); margin-top: 14px;
  }
  .contact-line + .contact-line { margin-top: 6px; }
  .contact-line svg { width: 14px; height: 14px; flex: none; }
  .card-back .brand { position: absolute; left: 46px; bottom: 46px; }
  .card-back .brand-name { font-size: 30px; }
  .card-back .brand-name small { font-size: 14px; }
</style>
</head>
<body>

  <section class="card card-front" aria-label="Card front">
    <div class="brand">
      <span class="brand-mark"></span>
      <p class="brand-name">Quillmarsh<small>Property Solutions</small></p>
    </div>
    <div class="edge-band"><span class="red"></span><span class="blue"></span><span class="green"></span></div>
  </section>

  <section class="card card-back" aria-label="Card back">
    <div class="contact">
      <p class="person-name">Rosalind Opaleye</p>
      <p class="person-role">Property Investor</p>
      <p class="contact-line">+44(0)7700361752
        <svg viewBox="0 0 14 14" aria-hidden="true"><rect x="3" y="1" width="8" height="12" rx="1.5" fill="none" stroke="var(--green)" stroke-width="1.4"/><circle cx="7" cy="11" r=".8" fill="var(--green)"/></svg>
      </p>
      <p class="contact-line">rosalind.quillmarsh@brindlepost.co.uk
        <svg viewBox="0 0 14 14" aria-hidden="true"><rect x="1" y="3" width="12" height="8" fill="var(--green)"/><path d="M1 3 L7 8 L13 3" fill="none" stroke="#fff" stroke-width="1"/></svg>
      </p>
    </div>
    <div class="brand">
      <span class="brand-mark"></span>
      <p class="brand-name">Quillmarsh<small>Property Solutions</small></p>
    </div>
    <div class="edge-band"><span class="green"></span><span class="red"></span><span class="blue"></span></div>
  </section>

</body>
</html>
```